Online ticketing company needs new biz card design

Needing an updated business card to reflect our company, incorporating our existing logo and colour scheme (red, black, white). The design should communicate our modern, online, technology, innovation based company.

Details for card need to include the following:

Name
Position
Telephone and extension number
Mobile number
Email
Web address
Physical and/or postal address

Industry/Entity Type

Business

Font styles to use
Sans Serif

Requirements
Must have
• Clear, bold, eye catching design

```html
<!DOCTYPE html>
<html lang="en">
<head>
<meta charset="utf-8">
<title>Passly Business Card</title>
<link rel="stylesheet" href="https://fonts.googleapis.com/css2?family=Roboto+Condensed:wght@700&family=Arimo:wght@400&display=swap">
<style>
  :root {
    --card-red: #d2232a;
    --card-black: #0d0d0d;
    --card-white: #ffffff;
    --page-bg: #e9e9e9;
  }
  * { margin: 0; padding: 0; box-sizing: border-box; }
  html, body { width: 1200px; height: 1000px; overflow: hidden; }
  body {
    background: var(--page-bg);
    font-family: "Arimo", Arial, sans-serif;
    color: var(--card-white);
    position: relative;
  }
  .card {
    position: absolute;
    left: 210px;
    width: 780px;
    height: 450px;
    background: var(--card-red);
    border-radius: 44px;
    overflow: hidden;
    box-shadow: 0 8px 20px rgba(0,0,0,0.25);
  }
  .card--front { top: 30px; }
  .card--back { top: 520px; }

  .card__band {
    position: absolute;
    left: 0; right: 0; bottom: 0;
    height: 88px;
    background: var(--card-black);
    display: flex;
    align-items: center;
    justify-content: center;
  }
  .web-address {
    font-size: 30px;
    letter-spacing: 0.42em;
    padding-left: 0.42em;
  }
  .tagline { font-size: 22px; }

  .brand {
    position: absolute;
    display: flex;
    align-items: center;
    gap: 18px;
    font-family: "Roboto Condensed", "Arial Narrow", sans-serif;
    font-weight: 700;
    color: var(--card-white);
  }
  .brand__dot {
    border-radius: 50%;
    background: var(--card-black);
    flex: none;
  }
  .card--front .brand { left: 60px; top: 140px; font-size: 78px; }
  .card--front .brand__dot { width: 46px; height: 46px; }
  .card--back .brand {
    left: 0; right: 0; top: 120px;
    justify-content: center;
    font-size: 96px;
  }
  .card--back .brand__dot { width: 56px; height: 56px; }

  .contact {
    position: absolute;
    right: 56px;
    top: 48px;
    width: 320px;
    text-align: right;
  }
  .contact__name, .contact__role {
    font-family: "Roboto Condensed", "Arial Narrow", sans-serif;
    font-weight: 700;
    font-size: 31px;
    line-height: 1.1;
  }
  .contact__lines {
    margin-top: 20px;
    font-size: 24px;
    line-height: 1.3;
  }
  .contact__rule {
    height: 2px;
    background: var(--card-black);
    margin: 16px 0 14px;
  }
  .contact__address {
    font-size: 22px;
    line-height: 1.25;
    font-style: normal;
  }
</style>
</head>
<body>

  <section class="card card--front" aria-label="Business card front">
    <div class="brand"><span class="brand__dot"></span><span class="brand__name">PASSLY</span></div>
    <div class="contact">
      <p class="contact__name">Liam Carter</p>
      <p class="contact__role">Vice President</p>
      <div class="contact__lines">
        <p>09.482.2000 ext 417</p>
        <p>55.123.4567</p>
        <p>lcarter@passly.co.nz</p>
      </div>
      <div class="contact__rule"></div>
      <address class="contact__address">
        PO Box 18264, Grey Lynn<br>Auckland<br>New Zealand
      </address>
    </div>
    <div class="card__band"><span class="web-address">www.passly.co.nz</span></div>
  </section>

  <section class="card card--back" aria-label="Business card back">
    <div class="brand"><span class="brand__dot"></span><span class="brand__name">PASSLY</span></div>
    <div class="card__band"><span class="tagline">Say goodbye to costly, outdated ways of buying your tickets!</span></div>
  </section>

</body>
</html>
```